Biz Card Design TPVC

New business card for a new company.
Logo was completed by a designer on ArtFlock and looking to continue requesting additional services.
Company Name: Tidal Prime Voltage Collective
Although this company is starting in Canada, we will be moving towards a global presence within the next 6 months.
Key elements to this business are as follows.
Energy Procurement
Energy Reduction Services
Demand Side Consulting
Energy Efficiency Consulting
Saving Clients Money
Helping Them Go "Green"
Managing Their Energy Requirements
Basically the goal for our company is to find the best procurement solution for our clients and reduce their energy consumption. This reduces their expenses and the amount of greenhouse gas they produce on a daily basis.
I have been in the energy footprint for the last 20 years and know that most companies are looking to "do whatever is necessary to get them to sign on the dotted line". I would prefer to walk away from a client that I can't help than to put them into a situation that they will regret for years to come. This is where the "TIDAL" part of the company name comes from.
The following is a catch phrase that encompasses what we do.
"Reducing your carbon footprint & energy bill at the same time!"
The back of the card needs to have this statement along with some sort of illustration. The back is a playground for creative ideas.
The front of the card needs the following.
Logo.
First & Last Name (Gus Marwick)
Title (Energy Warrior)
Phone Number (555) 314-2768
Fax Number (555) 862-4091
Email Address gus@tidalprimevoltage.example
Address 47 Orchard Lane Toronto Ontario K4P 2Z7
I want it to be a card that is remembered when any of my staff give it to a customer. It HAS to stand out.
Target Market(s)
Business Owners, Decision Makers, 30 to 65+
Industry/Entity Type
Business
Look and feel
Each slider illustrates characteristics of the customer's brand and the style your logo design should communicate.

```html
<!DOCTYPE html>
<html lang="en">
<head>
<meta charset="utf-8">
<title>Tidal Prime Voltage Collective – Business Card</title>
<link rel="stylesheet" href="https://fonts.googleapis.com/css2?family=Ubuntu:wght@500;700&family=Open+Sans:wght@400;600&display=swap">
<style>
  :root {
    --page: #e9e6e1;
    --blue: #3d6fb8;
    --blue-deep: #2f5ea6;
    --blue-band: #3b6cb5;
    --blue-faint: #4a86c6;
    --green: #2f9a3c;
    --green-light: #8cc86a;
    --white: #ffffff;
    --ink-blue: #3461ad;
  }
  * { box-sizing: border-box; margin: 0; padding: 0; }
  html, body { width: 1200px; height: 900px; overflow: hidden; }
  body {
    background: var(--page);
    font-family: "Open Sans", Arial, sans-serif;
    position: relative;
  }
  .card {
    position: absolute;
    width: 540px;
    height: 309px;
    overflow: hidden;
    box-shadow: 0 6px 18px rgba(0,0,0,0.25);
  }
  .card-back { left: 40px; top: 296px; background: linear-gradient(160deg, var(--blue-deep), var(--blue) 60%, #3c73bf); }
  .card-front { left: 620px; top: 296px; background: var(--white); }
  .card svg.shapes { position: absolute; inset: 0; }

  /* back */
  .dollar-mark {
    position: absolute; left: 10px; top: -40px;
    font-family: "Ubuntu", sans-serif; font-weight: 700;
    font-size: 330px; line-height: 1; color: var(--blue-faint); opacity: 0.75;
  }
  .back-name {
    position: absolute; left: 0; right: 0; top: 112px;
    text-align: center;
    font-family: "Ubuntu", sans-serif; font-weight: 700;
    font-size: 25px; color: var(--white); letter-spacing: -0.3px;
  }
  .back-band {
    position: absolute; left: 0; right: 0; bottom: 0; height: 40px;
    background: var(--blue-band);
    border-top: 1px solid rgba(255,255,255,0.15);
    color: var(--white); font-size: 14.5px;
    display: flex; align-items: center; justify-content: center;
  }

  /* front */
  .front-name-block {
    position: absolute; left: 14px; top: 112px; width: 280px;
    text-align: center;
    font-family: "Ubuntu", sans-serif; font-weight: 700;
    font-size: 18px; color: var(--ink-blue); letter-spacing: -0.3px;
  }
  .person { position: absolute; right: 100px; top: 16px; text-align: right; color: var(--ink-blue); }
  .person-name { font-family: "Ubuntu", sans-serif; font-weight: 500; font-size: 18px; line-height: 1.1; }
  .person-title { font-family: "Ubuntu", sans-serif; font-weight: 500; font-size: 12px; }
  .contacts {
    position: absolute; right: 16px; top: 90px;
    list-style: none; text-align: right;
    color: var(--white); font-size: 11px; line-height: 20px;
  }
  .contacts li { display: flex; justify-content: flex-end; align-items: center; gap: 5px; white-space: nowrap; }
  .contacts svg { width: 11px; height: 11px; fill: var(--white); flex: none; }
  .front-tagline {
    position: absolute; right: 16px; bottom: 14px;
    color: var(--white); font-size: 11px; white-space: nowrap;
  }
</style>
</head>
<body>

<section class="card card-back" aria-label="Card back">
  <div class="dollar-mark" aria-hidden="true">$</div>
  <div class="back-name">Tidal Prime Voltage Collective</div>
  <p class="back-band">"Reducing your carbon footprint &amp; energy bill at the same time!"</p>
</section>

<section class="card card-front" aria-label="Card front">
  <svg class="shapes" viewBox="0 0 540 309" aria-hidden="true">
    <defs>
      <linearGradient id="swoosh" x1="0" y1="1" x2="1" y2="0">
        <stop offset="0" stop-color="var(--green)"/>
        <stop offset="1" stop-color="var(--green-light)"/>
      </linearGradient>
    </defs>
    <path d="M512 0 C 355 108, 140 200, 2 309 L540 309 L540 0 Z" fill="url(#swoosh)"/>
    <path d="M532 0 C 372 110, 160 200, 22 309 L540 309 L540 0 Z" fill="var(--white)"/>
    <path d="M540 0 C 380 110, 170 200, 30 309 L540 309 Z" fill="var(--blue)"/>
  </svg>

  <div class="front-name-block">Tidal Prime Voltage Collective</div>

  <div class="person">
    <p class="person-name">Gus Marwick</p>
    <p class="person-title">Energy Warrior</p>
  </div>

  <ul class="contacts">
    <li>(555) 314-2768
      <svg viewBox="0 0 12 12"><path d="M2.5 1 L4.5 1 L5 3.5 L3.8 4.4 Q5 7 7.6 8.2 L8.5 7 L11 7.5 L11 9.5 Q10.5 11 9 11 Q1 10 1 3 Q1 1.5 2.5 1 Z"/></svg></li>
    <li>(555) 862-4091
      <svg viewBox="0 0 12 12"><path d="M1 3 H11 V11 H1 Z M3 1 H9 V3 H3 Z"/><rect x="3" y="5" width="6" height="1" fill="var(--blue)"/><rect x="3" y="7" width="6" height="1" fill="var(--blue)"/></svg></li>
    <li>gus@tidalprimevoltage.example
      <svg viewBox="0 0 12 12"><path d="M1 2.5 H11 V9.5 H1 Z"/><path d="M1 2.5 L6 6.5 L11 2.5" stroke="var(--blue)" stroke-width="1" fill="none"/></svg></li>
    <li>47 Orchard Lane Toronto Canada K4P 2Z7
      <svg viewBox="0 0 12 12"><path d="M6 1 L11.5 6 H10 V11 H7.2 V8 H4.8 V11 H2 V6 H0.5 Z"/></svg></li>
  </ul>

  <p class="front-tagline">"Reducing your carbon footprint &amp; energy bill at the same time!"</p>
</section>

</body>
</html>
```